Two wall artworks for physiotherapy clinic waiting room

We are a physiotherapy clinic located in Glebe, Sydney. We have a clinic that is within a beautiful heritage listed building and we have two blank white walls that need artwork. Each artwork will be 3000mm wide and 1200mm high. Our clinic is mostly white and I will include our brand's colours below. We are looking for bright, beautiful artworks that are consistent with our colours. One of the artworks should include our full logo including the text so that customers see the name of the clinic on their way into the waiting room. I will include our logo in the files below, as well as images of the clinic, the walls and some other signs that we have already. We would prefer artworks with nice patterns or graphics rather than images of people.

```html
<!DOCTYPE html>
<html lang="en">
<head>
<meta charset="UTF-8">
<title>Kestrel Physio – Waiting Room Artworks</title>
<link rel="stylesheet" href="https://fonts.googleapis.com/css2?family=Montserrat:wght@500;600&family=Source+Sans+3:ital,wght@1,400&display=swap">
<style>
  :root {
    --sheet: #ffffff;
    --sheet-edge: #3a3a3a;
    --teal: #39c6b8;
    --teal-light: #8ef5ea;
    --navy: #1b1464;
    --navy-light: #453c9e;
    --ink-on-art: #ffffff;
  }
  * { box-sizing: border-box; margin: 0; padding: 0; }
  html, body {
    width: 1200px;
    height: 1014px;
    overflow: hidden;
    background: var(--sheet);
  }
  .sheet {
    position: relative;
    width: 1200px;
    height: 1014px;
    border: 1px solid var(--sheet-edge);
    background: var(--sheet);
  }
  .artwork {
    position: absolute;
    left: 35px;
    width: 1132px;
    height: 453px;
    overflow: hidden;
  }
  .artwork--teal { top: 39px; background: var(--teal); }
  .artwork--navy { top: 532px; background: var(--navy); }

  .wave-pattern {
    position: absolute;
    inset: 0;
  }
  .artwork--teal .wave-pattern {
    background:
      linear-gradient(160deg, transparent 38%, rgba(142,245,234,0.35) 50%, transparent 62%),
      radial-gradient(ellipse 60% 45% at 22% 70%, rgba(142,245,234,0.28), transparent 70%),
      radial-gradient(ellipse 50% 45% at 80% 30%, rgba(142,245,234,0.28), transparent 70%),
      var(--teal);
  }
  .artwork--navy .wave-pattern {
    background:
      linear-gradient(160deg, transparent 38%, rgba(69,60,158,0.45) 50%, transparent 62%),
      radial-gradient(ellipse 60% 45% at 22% 70%, rgba(69,60,158,0.35), transparent 70%),
      radial-gradient(ellipse 50% 45% at 80% 30%, rgba(69,60,158,0.35), transparent 70%),
      var(--navy);
  }

  .brand {
    position: absolute;
    left: 94px;
    top: 60px;
    display: flex;
    align-items: center;
    color: var(--ink-on-art);
  }
  .brand-mark {
    width: 78px;
    height: 78px;
    margin-right: 24px;
  }
  .brand-text { display: flex; flex-direction: column; }
  .brand-name {
    font-family: "Montserrat", sans-serif;
    font-weight: 500;
    font-size: 60px;
    line-height: 1;
    letter-spacing: 0.5px;
  }
  .brand-tagline {
    font-family: "Montserrat", sans-serif;
    font-weight: 600;
    font-size: 17px;
    margin-top: 12px;
    margin-left: 4px;
  }
  .services {
    position: absolute;
    left: 112px;
    top: 162px;
    color: var(--ink-on-art);
    font-family: "Source Sans 3", sans-serif;
    font-style: italic;
    font-weight: 400;
    font-size: 27px;
    display: flex;
    align-items: center;
    gap: 14px;
  }
  .services .divider {
    display: inline-block;
    width: 1.5px;
    height: 28px;
    background: var(--ink-on-art);
  }
</style>
</head>
<body>
<main class="sheet">

  <section class="artwork artwork--teal">
    <div class="wave-pattern" role="img" aria-label="Flowing pale aqua wave line pattern sweeping across the teal background"></div>
    <div class="brand">
      <svg class="brand-mark" viewBox="0 0 78 78" aria-hidden="true"><circle cx="39" cy="39" r="33" fill="none" stroke="#ffffff" stroke-width="10"/></svg>
      <div class="brand-text">
        <span class="brand-name">Kestrel Physio</span>
        <span class="brand-tagline">Physiotherapy and Exercise Physiology</span>
      </div>
    </div>
    <p class="services">
      <span>Physiotherapy</span><span class="divider"></span>
      <span>Exercise Physiology</span><span class="divider"></span>
      <span>Classes</span>
    </p>
  </section>

  <section class="artwork artwork--navy">
    <div class="wave-pattern" role="img" aria-label="Flowing violet wave line pattern sweeping across the navy background"></div>
    <div class="brand">
      <svg class="brand-mark" viewBox="0 0 78 78" aria-hidden="true"><circle cx="39" cy="39" r="33" fill="none" stroke="#ffffff" stroke-width="10"/></svg>
      <div class="brand-text">
        <span class="brand-name">Kestrel Physio</span>
        <span class="brand-tagline">Physiotherapy and Exercise Physiology</span>
      </div>
    </div>
    <p class="services">
      <span>Physiotherapy</span><span class="divider"></span>
      <span>Exercise Physiology</span><span class="divider"></span>
      <span>Classes</span>
    </p>
  </section>

</main>
</body>
</html>
```